Nicht nur, dass ich mit dem Design sehr zufrieden war, auch Änderungswünsche wurden zeitnah und zu meiner vollen Zufriedenheit ausgeführt.
Zielgruppe
Ich schreibe Kriminalromane
Zielgruppe sind die Leser von Kriminalromanen, Regionalkrimis
Aufgabenstellung
Hier handelt es sich um eine Kindesentführung im ländlichen Raum (Bayerischer Wald) ein Mosaik von Inzest und Tod.
Der Titel in moderner Schrift, angelehnt an die Titel der Skandinavienkrimis, sollte auch in kleiner Abbildung gut lesbar sein.
Es kommen in Kürze zwei weitere Titel, ebenfalls Kriminalromane, das Cover sollte also so gestaltet sein, dass eine durchgängige Reihe möglich ist.

```html
<!DOCTYPE html>
<html lang="de">
<head>
<meta charset="utf-8">
<title>Die Akte Wendel – Buchcover</title>
<link rel="stylesheet" href="https://fonts.googleapis.com/css2?family=Arimo:wght@400;700&display=swap">
<style>
  :root {
    --canvas: #ececec;
    --cover-red: #c8161a;
    --label-red: #c8161a;
    --band-black: #050505;
    --white: #ffffff;
    --sky: #9fbcb8;
    --wall-warm: #b77a4c;
    --wall-grey: #a9a6a0;
    --road: #3a302b;
  }
  * { margin: 0; padding: 0; box-sizing: border-box; }
  html, body {
    width: 1200px;
    height: 960px;
    overflow: hidden;
    background: var(--canvas);
    font-family: "Arimo", Arial, sans-serif;
  }
  .book-cover {
    position: absolute;
    left: 267px;
    top: 40px;
    width: 666px;
    height: 880px;
    background: var(--cover-red);
  }
  .cover-photo {
    position: absolute;
    left: 66px;
    top: 64px;
    width: 535px;
    height: 757px;
    background: linear-gradient(180deg,
      var(--sky) 0%,
      #b7c9bd 18%,
      var(--wall-warm) 38%,
      var(--wall-grey) 52%,
      #8f7f70 60%,
      #5a4a40 68%,
      var(--road) 82%,
      #2a221e 100%);
    overflow: hidden;
  }
  .photo-band {
    position: absolute;
    left: 0;
    bottom: 0;
    width: 100%;
    height: 36px;
    background: var(--band-black);
  }
  .title-block {
    position: absolute;
    left: 0;
    top: 514px;
    width: 100%;
    display: flex;
    flex-direction: column;
    align-items: center;
  }
  .title-line {
    display: inline-block;
    background: var(--label-red);
    color: var(--white);
    font-weight: 700;
    font-size: 74px;
    line-height: 82px;
    letter-spacing: 0.5px;
    padding: 0 12px;
    margin-bottom: 6px;
    white-space: nowrap;
  }
  .byline {
    display: inline-block;
    background: var(--label-red);
    color: var(--white);
    font-weight: 400;
    font-size: 14px;
    line-height: 27px;
    padding: 0 9px;
    margin-top: 4px;
    white-space: nowrap;
  }
</style>
</head>
<body>
  <div class="book-cover">
    <div class="cover-photo" role="img" aria-label="Foto: Dorfstraße mit verputztem Bauernhaus und grauem Anbau im warmen Abendlicht, Strommasten und Kondensstreifen am Himmel">
      <div class="photo-band"></div>
      <div class="title-block">
        <h1 class="title-line">DIE AKTE</h1>
        <h1 class="title-line">WENDEL</h1>
        <p class="byline">Kriminalroman | Tobias Hallstein</p>
      </div>
    </div>
  </div>
</body>
</html>
```